Veridane Works, Inc. - Update our Website

Veridane Works needs a website to help our customers to navigate through our services efficiently. Our existing website is at www.verowk.example

We would like to explain our services with content and pictures (photographs) that distinguishes our products and services from our competition.

The website design must implement a strategy to focus on our Contract Labeling services.

With this new design we would like to attract new customers and ensure that our existing customers are fully informed with our latest offerings.

```html
<!DOCTYPE html>
<html lang="en">
<head>
<meta charset="utf-8">
<title>Veridane Works, Inc.</title>
<link rel="stylesheet" href="https://fonts.googleapis.com/css2?family=Open+Sans:wght@300;400;600;700;800&display=swap">
<style>
  :root {
    --ink: #2b2d35;
    --muted: #6a6c72;
    --brand-blue: #1b76b2;
    --brand-blue-dark: #13609a;
    --accent-green: #6cbd0c;
    --hero-lime: #e4f6b5;
    --hero-peach: #fcca8c;
    --white: #ffffff;
  }
  * { box-sizing: border-box; margin: 0; padding: 0; }
  html, body { width: 1200px; height: 921px; overflow: hidden; background: var(--white); }
  body { font-family: "Open Sans", sans-serif; color: var(--ink); position: relative; }

  .site-header { position: absolute; left: 0; top: 0; width: 1200px; height: 93px; }
  .brand { position: absolute; left: 172px; top: 26px; display: flex; align-items: center; gap: 10px; }
  .brand-dot { width: 40px; height: 40px; border-radius: 50%; background: var(--accent-green); }
  .brand-name { font-size: 19px; font-weight: 800; letter-spacing: 0.5px; color: #1c1c1c; text-transform: uppercase; }
  .main-nav { position: absolute; right: 171px; top: 36px; display: flex; align-items: center; font-size: 12px; text-transform: uppercase; }
  .main-nav a { color: var(--ink); text-decoration: none; padding-bottom: 2px; }
  .main-nav .sep { display: inline-block; width: 1px; height: 10px; background: var(--ink); margin: 0 15px; }
  .main-nav a.active { color: var(--accent-green); border-bottom: 2px solid var(--accent-green); }

  .hero { position: absolute; left: 0; top: 93px; width: 1200px; height: 348px;
    background: linear-gradient(180deg, #1f7cb8 0%, #1a72ad 60%, #2080bd 100%);
    box-shadow: inset 0 8px 10px -6px rgba(0,0,0,0.35); }
  .hero-copy { position: absolute; left: 0; width: 1200px; top: 62px; text-align: center; color: var(--white); }
  .hero-lead { font-size: 41px; font-weight: 300; line-height: 46px; }
  .hero-big { font-size: 54px; font-weight: 700; line-height: 49px; }
  .hl-lime { color: var(--hero-lime); }
  .hl-peach { color: var(--hero-peach); }
  .hero-arrow { position: absolute; top: 149px; width: 48px; height: 48px; }
  .hero-arrow.prev { left: 44px; }
  .hero-arrow.next { right: 46px; }
  .hero-cta { position: absolute; left: 522px; top: 245px; width: 156px; height: 41px;
    border: 2px solid var(--white); color: var(--white); font-size: 12.5px; text-transform: uppercase;
    display: flex; align-items: center; justify-content: center; gap: 10px; text-decoration: none; }

  .services-title { position: absolute; top: 474px; left: 0; width: 1200px; text-align: center;
    font-size: 29px; font-weight: 400; color: var(--ink); }
  .services-rule { position: absolute; top: 524px; left: 551px; width: 99px; height: 4px; background: var(--brand-blue); }

  .service-card { position: absolute; top: 560px; width: 271px; }
  .service-card:nth-of-type(1) { left: 171px; }
  .service-card:nth-of-type(2) { left: 464px; }
  .service-card:nth-of-type(3) { left: 757px; }
  .service-photo { width: 271px; height: 163px; }
  .photo-typing { background: linear-gradient(135deg, #6d6a66, #c9c4c0 55%, #eeeae6); }
  .photo-meeting { background: linear-gradient(135deg, #d9dde2, #b9c2cc 50%, #eef0f2); }
  .photo-writing { background: linear-gradient(135deg, #e9e6e3, #bfb6b0 50%, #f4f2f0); }
  .service-name { margin-top: 14px; font-size: 17px; font-weight: 600; line-height: 21px; text-transform: uppercase; color: var(--ink); }
  .service-text { margin-top: 11px; font-size: 11.5px; line-height: 19px; color: var(--muted); width: 232px; text-align: justify; }
  .service-more { position: absolute; top: 307px; left: 1px; width: 65px; height: 32px;
    border: 2px solid var(--accent-green); color: var(--accent-green); font-size: 13.5px;
    display: flex; align-items: center; justify-content: center; text-decoration: none; text-transform: uppercase; }
</style>
</head>
<body>
  <header class="site-header">
    <div class="brand"><span class="brand-dot"></span><span class="brand-name">Veridane Works, Inc.</span></div>
    <nav class="main-nav">
      <a href="#" class="active">Home</a><span class="sep"></span>
      <a href="#">About</a><span class="sep"></span>
      <a href="#">Products</a><span class="sep"></span>
      <a href="#">Services</a><span class="sep"></span>
      <a href="#">User Support</a><span class="sep"></span>
      <a href="#">Contact</a>
    </nav>
  </header>

  <section class="hero" role="img" aria-label="Blue-tinted photo of a laboratory workspace">
    <div class="hero-copy">
      <p class="hero-lead">We specializes in providing</p>
      <p class="hero-big"><span class="hl-lime">Products &amp; Services</span> to</p>
      <p class="hero-big">the <span class="hl-peach">Pharmaceutical</span> industry</p>
    </div>
    <svg class="hero-arrow prev" viewBox="0 0 48 48" aria-hidden="true">
      <circle cx="24" cy="24" r="22.5" fill="none" stroke="#fff" stroke-width="2.5"/>
      <path d="M35 24H13M22 14l-10 10 10 10" fill="none" stroke="#fff" stroke-width="2.5" stroke-linecap="round" stroke-linejoin="round"/>
    </svg>
    <svg class="hero-arrow next" viewBox="0 0 48 48" aria-hidden="true">
      <circle cx="24" cy="24" r="22.5" fill="none" stroke="#fff" stroke-width="2.5"/>
      <path d="M13 24h22M26 14l10 10-10 10" fill="none" stroke="#fff" stroke-width="2.5" stroke-linecap="round" stroke-linejoin="round"/>
    </svg>
    <a class="hero-cta" href="#">
      <svg width="22" height="18" viewBox="0 0 22 18" aria-hidden="true">
        <path d="M1 7h4v10H1zM5 8l4-6c1-1 2 0 2 1l-1 4h9c1 0 2 1 2 2s-1 2-2 2h-1c1 0 1 2 0 2h-1c1 0 1 2 0 2H6" fill="none" stroke="#fff" stroke-width="1.5" stroke-linejoin="round"/>
      </svg>
      Learn More
    </a>
  </section>

  <h2 class="services-title">OUR SERVICES</h2>
  <div class="services-rule"></div>

  <article class="service-card">
    <div class="service-photo photo-typing" role="img" aria-label="Hands typing on a laptop keyboard"></div>
    <h3 class="service-name">VeriBook™-Clinical<br>Booklet Labels</h3>
    <p class="service-text">VeriBook™ labels are multi-page clinical labels used to address the needs of multi-language studies...</p>
    <a class="service-more" href="#">More</a>
  </article>
  <article class="service-card">
    <div class="service-photo photo-meeting" role="img" aria-label="Two colleagues reviewing documents at a laptop"></div>
    <h3 class="service-name">VeriServ™ - Contract<br>Clinical Label</h3>
    <p class="service-text">VeriServ™ is a contract clinical label generation service that provides you with ready to apply clinical labels...</p>
    <a class="service-more" href="#">More</a>
  </article>
  <article class="service-card">
    <div class="service-photo photo-writing" role="img" aria-label="Hand writing on a paper form with a pen"></div>
    <h3 class="service-name">Clinical Randomizations<br>System</h3>
    <p class="service-text">Our systems can create randomization data for all types of CTM requirements. Patient randomization...</p>
    <a class="service-more" href="#">More</a>
  </article>
</body>
</html>
```